Design a template for our corporate publications

Design a template for corporate publications, such as monthly newsletters, updates and services sheets.

The design must be:

1) eye catching / exciting;
2) Professional;
3) Unique (no templates please);
4) Utilise our logo;
5) Easy to amend by none designers;
6) Easy to save in PDF - these will be printed and sent electronically;
7) Easily distinguishable from our competitors.

I have attached two examples of the kind of releases our company make: (1) our quarterly update - please do not copy the table into the document, we do not release our publications in tabular format; and (2) our commentary on a regulatory update. In addition, I have included our logo.

You can find further information about our company at [login to view URL]

```html
<!DOCTYPE html>
<html lang="en">
<head>
<meta charset="utf-8">
<title>Corporate Publications Template</title>
<link href="https://fonts.googleapis.com/css2?family=Raleway:wght@300;400;600&family=Open+Sans:wght@400;600;700&display=swap" rel="stylesheet">
<style>
  :root{
    --backdrop:#d6d6d6;
    --paper:#ffffff;
    --paper-shade:#f1f1f1;
    --ink:#3b3b3b;
    --ink-soft:#7a7a7a;
    --rule:#c9c9c9;
    --slate:#4a4a4a;
    --slate-mid:#8c8c8c;
    --slate-light:#b8b8b8;
    --brand-blue:#2f9fd8;
    --brand-blue-light:#5bb8e6;
    --title-grey:#ffffff;
  }
  *{box-sizing:border-box;margin:0;padding:0}
  html,body{width:1200px;height:795px;overflow:hidden}
  body{background:var(--backdrop);font-family:'Open Sans',sans-serif;color:var(--ink);position:relative}
  .quadrant{position:absolute;width:600px;height:397px}
  .q-cover{left:0;top:0}
  .q-spread-one{left:600px;top:0}
  .q-title{left:0;top:398px;background:#c4c4c4}
  .q-spread-two{left:600px;top:398px}
  .page{position:absolute;width:230px;height:310px;background:var(--paper);box-shadow:0 4px 14px rgba(0,0,0,.18);overflow:hidden}
  .spread{position:absolute;left:70px;top:44px;width:460px;height:310px;display:flex;box-shadow:0 4px 14px rgba(0,0,0,.18)}
  .spread .page{position:relative;box-shadow:none}
  .spread .page-left{background:linear-gradient(90deg,var(--paper) 85%,var(--paper-shade))}
  .spread .page-right{background:linear-gradient(90deg,var(--paper-shade),var(--paper) 15%)}

  /* cover */
  .cover{left:185px;top:44px}
  .brand-lockup{display:flex;align-items:center;gap:6px;font-family:'Raleway',sans-serif;font-weight:400;color:var(--slate)}
  .brand-mark{width:10px;height:10px;background:var(--brand-blue)}
  .cover .brand-lockup{position:absolute;left:24px;top:86px;font-size:11px}
  .cover-band{position:absolute;left:0;top:110px;width:100%;height:20px;background:var(--slate);color:#fff;font-family:'Raleway',sans-serif;font-size:10px;line-height:20px;padding-left:30px;letter-spacing:.3px}
  .cover-art{position:absolute;right:26px;top:196px;width:48px;height:68px;background:linear-gradient(180deg,#bfe2f5,#6fb6e0);border:2px solid #e4e4e4}

  /* spread one left */
  .tile{position:absolute}
  .summary{position:absolute;right:18px;top:150px;text-align:right;font-family:'Raleway',sans-serif;font-weight:300;font-size:13px;line-height:1.3;color:var(--ink)}
  .page-left .brand-lockup.summary-brand{position:absolute;right:18px;top:232px;font-size:9px}
  .date-block{position:absolute;right:0;top:0;width:120px;height:30px;background:var(--slate-mid);color:#fff;font-weight:700;font-size:10px;text-align:right;padding:14px 10px 0 0;letter-spacing:.4px}
  .article{position:absolute;left:16px;right:14px}
  .article h3{font-size:7.5px;font-weight:600;color:var(--brand-blue);margin-bottom:5px;line-height:1.3}
  .article h4{font-size:6px;font-weight:700;color:var(--ink);margin:6px 0 3px;text-transform:uppercase}
  .article p{font-size:6px;line-height:1.5;color:var(--ink-soft)}
  .page-footer{position:absolute;left:16px;bottom:14px;font-size:6px}

  /* spread two */
  .blue-band{position:absolute;left:0;top:0;width:100%;height:44px;background:linear-gradient(180deg,var(--brand-blue-light),var(--brand-blue))}
  .band-date{position:absolute;color:#fff;font-weight:700;font-size:10px;letter-spacing:.4px;line-height:1.15}
  .page-left .band-date{left:14px;top:22px}
  .page-right .band-date{right:14px;top:12px;text-align:right}

  .template-title{position:absolute;left:56px;top:112px;font-family:'Raleway',sans-serif;font-weight:300;font-size:48px;line-height:1.22;color:var(--title-grey)}
</style>
</head>
<body>

<section class="quadrant q-cover">
  <article class="page cover">
    <div class="brand-lockup"><span class="brand-mark"></span>Northgate Compliance Partners</div>
    <div class="cover-band">NCP Regulatory Digest</div>
    <div class="cover-art" role="img" aria-label="Illustration of an open door revealing a blue sky"></div>
  </article>
</section>

<section class="quadrant q-spread-one">
  <div class="spread">
    <article class="page page-left">
      <div class="tile" style="left:0;top:18px;width:38px;height:38px;background:var(--slate-mid)"></div>
      <div class="tile" style="left:38px;top:18px;width:38px;height:38px;background:var(--brand-blue)"></div>
      <div class="tile" style="left:76px;top:0;width:38px;height:56px;background:var(--slate)"></div>
      <div class="tile" style="left:38px;top:56px;width:76px;height:38px;background:var(--slate-light)"></div>
      <div class="tile" style="left:180px;top:112px;width:50px;height:26px;background:var(--slate-light)"></div>
      <div class="tile" style="left:170px;top:262px;width:60px;height:22px;background:var(--slate-mid)"></div>
      <p class="summary">Summary of Q3 2013<br>Regulatory Updates<br>from the Financial<br>Crime Division</p>
      <div class="brand-lockup summary-brand"><span class="brand-mark"></span>Northgate Compliance Partners</div>
    </article>
    <article class="page page-right">
      <div class="date-block">20 SEPTEMBER</div>
      <div class="article" style="top:44px">
        <h3>Regulator publishes final guidance on financial crime systems</h3>
        <p>The regulator has set out updated expectations for firms on anti-money laundering controls, sanctions screening and fraud prevention.</p>
        <h4>Key points for regulated firms</h4>
        <p>Firms should review governance, risk assessments and staff training before the year end.</p>
      </div>
      <div class="brand-lockup page-footer"><span class="brand-mark" style="width:7px;height:7px"></span>Northgate Compliance Partners</div>
    </article>
  </div>
</section>

<section class="quadrant q-title">
  <h1 class="template-title">Corporate<br>Publications<br>Template</h1>
</section>

<section class="quadrant q-spread-two">
  <div class="spread">
    <article class="page page-left">
      <div class="blue-band"><span class="band-date">25<br>SEPTEMBER</span></div>
      <div class="article" style="top:58px">
        <h3>Consultation on updated sanctions reporting duties</h3>
        <p>Proposed changes would require firms to report suspected breaches sooner and keep fuller records of screening decisions.</p>
        <h4>What firms should do now</h4>
        <p>Map current reporting routes and brief senior managers on the new timelines.</p>
      </div>
      <div class="brand-lockup page-footer"><span class="brand-mark" style="width:7px;height:7px"></span>Northgate Compliance Partners</div>
    </article>
    <article class="page page-right">
      <div class="blue-band"><span class="band-date">27<br>SEPTEMBER</span></div>
      <div class="article" style="top:58px">
        <h3>New thematic review of anti-bribery controls announced</h3>
        <p>Reviewers will visit a sample of firms to test due diligence on agents, gifts and hospitality.</p>
        <h4>Next steps</h4>
        <p>Gather evidence of recent control testing ahead of any visit.</p>
      </div>
    </article>
  </div>
</section>

</body>
</html>
```